The Lark Coffee Bags for Retail Sale

We need three retail coffee bags designed for The Lark Bourbon & Coffee.

I have included the spec sheet.

We would like it to match our menu- attached here.

Here is each bag:

#1. Text:
The Meridian Blend
Espresso
Central & South American
Considered their “Founder's” coffee, this popular blend is wonderful for both espresso and drip-brewed coffee. It is full-bodied and rich without bitterness. The flavor is broad and tangy, with great aromatic dimension.
Notes:
Ideally, we would like the outline of the ship in the same style as the building outline from our menu. We want the background of this bag in a jewel toned teal color and gold. I will include an example of the teal color.

#2. Text:
The Lanternhook Blend
Drip
French & Indonesian
Sweet, smoky, smooth and chocolaty. It begins with a French Roast, with its distinctive smoky qualities, and mellowed it with a chocolaty Vienna-roasted Indonesian for an eye-opening blend that offers the best of both worlds: a bold and subtle morning brew.
Note: This can use the same outline as the menu of the Pellingham Building. We would like the background black on this bag.

#3. Text:
RUVANO DECAF Alpine Clear® Process
Earthy tones, smooth and sweet, mild acidity, and creamy texture.
This Alpine Clear® Process decaf is carefully roasted to bring out rich flavors. You'll find it hard to believe that you're drinking a decaffeinated coffee.

All bags must include the following information.

Roasted and Packaged by Brackwell Coffee Roasters
Langley, WA 98417

NET WT 12oz (340g)

We also want all bags to have our logo and, on the back, the Brackwell Coffee logo as they are the providers of the coffee.

Target Market(s)

Upscale Coffee Patrons

Industry/Entity Type

Coffee

Font styles to use
Serif

Requirements
Must have
• Correct colors, logo, blend name and tasting notes and legal retail notes
Nice to have
• Unique designs
Should not have
• anything outside the predescribed colors

```html
<!DOCTYPE html>
<html lang="en">
<head>
<meta charset="utf-8">
<title>The Lark Bourbon &amp; Coffee — Retail Coffee Bags</title>
<link href="https://fonts.googleapis.com/css2?family=Montserrat:wght@600;800&family=Open+Sans:wght@600;700&family=Oswald:wght@600&display=swap" rel="stylesheet">
<style>
  :root{
    --backdrop:#ebe3c6;
    --gold:#d9b756;
    --gold-light:#f3e29a;
    --gold-deep:#a9852d;
    --burgundy:#6e1e22;
    --burgundy-dark:#561519;
    --onyx:#141414;
    --onyx-soft:#2a2a2a;
    --teal:#0b6b66;
    --teal-dark:#07514d;
    --teal-ink:#033a37;
    --cream:#f7f1df;
  }
  *{box-sizing:border-box;margin:0;padding:0}
  html,body{width:1166px;height:1200px;overflow:hidden}
  body{background:var(--backdrop);font-family:"Open Sans",sans-serif;display:flex;align-items:center;justify-content:center}
  .lineup{display:flex;gap:28px}
  .bag{display:flex;width:344px;height:940px;box-shadow:0 18px 36px rgba(80,60,20,.18)}
  .gusset{width:46px;background:linear-gradient(180deg,var(--gold-light),var(--gold) 45%,var(--gold-deep));display:flex;align-items:center;justify-content:center}
  .gusset-label{writing-mode:vertical-rl;transform:rotate(180deg);font-family:"Montserrat",sans-serif;font-weight:800;font-size:11px;letter-spacing:.06em;padding:14px 0;border-top:1px solid currentColor;border-bottom:1px solid currentColor;white-space:nowrap}
  .face{flex:1;position:relative;display:flex;flex-direction:column;align-items:center;color:var(--gold);overflow:hidden}
  .bag--decaf .face{background:linear-gradient(170deg,var(--burgundy),var(--burgundy-dark))}
  .bag--decaf .gusset-label{color:var(--burgundy)}
  .bag--drip .face{background:linear-gradient(170deg,var(--onyx-soft),var(--onyx) 60%)}
  .bag--drip .gusset-label{color:var(--onyx)}
  .bag--espresso .face{background:linear-gradient(170deg,var(--teal),var(--teal-dark))}
  .bag--espresso .gusset-label{color:var(--teal-dark)}
  .valve{position:absolute;top:190px;width:40px;height:40px;border-radius:50%;box-shadow:inset 0 0 0 1px rgba(0,0,0,.25);z-index:2}
  .valve::after{content:"";position:absolute;left:18px;top:18px;width:4px;height:4px;border-radius:50%;background:rgba(0,0,0,.5)}
  .brand{position:relative;z-index:2;margin-top:300px;display:flex;flex-direction:column;align-items:center;gap:4px}
  .brand-mark{width:14px;height:14px;border:2px solid var(--gold)}
  .brand-name{font-family:"Montserrat",sans-serif;font-weight:800;font-size:22px;letter-spacing:.08em}
  .brand-tag{font-family:"Montserrat",sans-serif;font-weight:600;font-size:8px;letter-spacing:.12em}
  .blend-name{position:relative;z-index:2;margin-top:34px;padding:0 14px;font-family:"Montserrat",sans-serif;font-weight:800;font-size:34px;line-height:1.12;text-align:center;text-transform:uppercase}
  .blend-name--long{font-size:28px;line-height:1.36}
  .scene{position:absolute;left:0;right:0;bottom:0;height:340px;z-index:1}
  .bag--decaf .scene{background:linear-gradient(180deg,rgba(217,183,86,0) 0%,rgba(217,183,86,.18) 45%,rgba(217,183,86,.32) 100%)}
  .bag--drip .scene{height:300px;background:linear-gradient(180deg,rgba(217,183,86,0) 0%,rgba(217,183,86,.16) 45%,rgba(217,183,86,.3) 100%)}
  .bag--espresso .scene{height:380px;background:linear-gradient(180deg,rgba(3,58,55,0) 0%,rgba(3,58,55,.45) 40%,rgba(3,58,55,.7) 100%)}
  .label-box{position:absolute;z-index:3;top:655px;left:34px;right:34px;border:1.5px solid var(--gold);padding:24px 10px 16px;text-align:center;color:var(--cream)}
  .label-method{position:absolute;top:-16px;left:50%;transform:translateX(-50%);padding:0 6px;font-family:"Oswald",sans-serif;font-weight:600;font-size:24px;line-height:1;color:#fff;white-space:nowrap}
  .bag--drip .label-method{background:#1a1a18}
  .bag--espresso .label-method{background:var(--teal-dark)}
  .label-origin{font-weight:600;font-size:16px;line-height:1.35;text-transform:uppercase}
  .bag--decaf .label-box{padding:20px 10px}
  .net-weight{position:absolute;z-index:3;bottom:26px;font-weight:700;font-size:12px;line-height:1.25;text-align:center;color:var(--cream)}
</style>
</head>
<body>
<main class="lineup">

  <article class="bag bag--decaf">
    <div class="gusset"><span class="gusset-label">THE RUVANO DECAF</span></div>
    <div class="face">
      <span class="valve"></span>
      <div class="brand"><span class="brand-mark"></span><span class="brand-name">THE LARK</span><span class="brand-tag">BOURBON &amp; COFFEE</span></div>
      <h2 class="blend-name">The<br>Ruvano<br>Decaf</h2>
      <div class="scene" role="img" aria-label="Gold line drawing of the Pellingham Building"></div>
      <div class="label-box"><p class="label-origin">Alpine Clear®<br>Process</p></div>
      <p class="net-weight">NET WT 12oz<br>(340G)</p>
    </div>
  </article>

  <article class="bag bag--drip">
    <div class="gusset"><span class="gusset-label">THE LANTERNHOOK BLEND</span></div>
    <div class="face">
      <span class="valve"></span>
      <div class="brand"><span class="brand-mark"></span><span class="brand-name">THE LARK</span><span class="brand-tag">BOURBON &amp; COFFEE</span></div>
      <h2 class="blend-name blend-name--long">The<br>Lanternhook<br>Blend</h2>
      <div class="scene" role="img" aria-label="Gold line drawing of the Pellingham Building roof and arched windows"></div>
      <div class="label-box"><span class="label-method">DRIP</span><p class="label-origin">French &amp;<br>Indonesian</p></div>
      <p class="net-weight">NET WT 12oz<br>(340G)</p>
    </div>
  </article>

  <article class="bag bag--espresso">
    <div class="gusset"><span class="gusset-label">THE MERIDIAN BLEND</span></div>
    <div class="face">
      <span class="valve"></span>
      <div class="brand"><span class="brand-mark"></span><span class="brand-name">THE LARK</span><span class="brand-tag">BOURBON &amp; COFFEE</span></div>
      <h2 class="blend-name">The<br>Meridian<br>Blend</h2>
      <div class="scene" role="img" aria-label="Dark line drawing of a ship's deck outline"></div>
      <div class="label-box"><span class="label-method">ESPRESSO</span><p class="label-origin">Central &amp; South<br>American</p></div>
      <p class="net-weight">NET WT 12oz<br>(340G)</p>
    </div>
  </article>

</main>
</body>
</html>
```